Brisket Glazing

Modern glazing company specializing in commercial fit outs, pool fencing, frameless showers and glass splash backs, im after a very young/modern logo, it doesnt have to be revelent to glazing and a classy "boss like" design for the card. thank you in advanced
Updates

im thinking carbon fiber back ground or something along that line with bright orange wording or something maybe, open to suggestions 

Industry/Entity Type

Fencing

Contact Information for Business Card

company name, name, phone and products

```html
<!DOCTYPE html>
<html lang="en">
<head>
<meta charset="UTF-8">
<title>Brisket Glazing – Business Card</title>
<link href="https://fonts.googleapis.com/css2?family=Exo+2:wght@600&family=Open+Sans:wght@400&display=swap" rel="stylesheet">
<style>
  :root {
    --page-bg: #ffffff;
    --card-top: #2b2e31;
    --card-bottom: #1c1e20;
    --brand-orange: #f0691f;
    --orange-deep: #d9531a;
    --silver: #c9ccce;
    --silver-dark: #8d9194;
    --text-light: #f2f2f2;
    --square-faint: rgba(240, 105, 31, 0.38);
  }
  * { margin: 0; padding: 0; box-sizing: border-box; }
  html, body {
    width: 1200px;
    height: 900px;
    overflow: hidden;
    background: var(--page-bg);
  }
  .canvas {
    position: relative;
    width: 1200px;
    height: 900px;
  }
  .card {
    position: absolute;
    top: 290px;
    width: 540px;
    height: 310px;
    border-radius: 24px;
    overflow: hidden;
    background: linear-gradient(160deg, var(--card-top), var(--card-bottom));
    box-shadow: 0 18px 30px rgba(0, 0, 0, 0.18);
  }
  .card--front { left: 40px; }
  .card--back { left: 620px; }

  /* front */
  .brand {
    position: absolute;
    left: 0;
    right: 0;
    top: 70px;
    display: flex;
    flex-direction: column;
    align-items: center;
  }
  .brand__square {
    width: 84px;
    height: 84px;
    background: var(--brand-orange);
  }
  .brand__name {
    margin-top: 26px;
    font-family: "Exo 2", sans-serif;
    font-weight: 600;
    font-size: 46px;
    letter-spacing: 0.5px;
    color: var(--brand-orange);
    white-space: nowrap;
  }
  .edge-band {
    position: absolute;
    left: 0;
    right: 0;
    bottom: 0;
    height: 38px;
  }

  /* back */
  .accent-square {
    position: absolute;
    left: 140px;
    top: 30px;
    width: 270px;
    height: 250px;
    background: var(--square-faint);
  }
  .contact {
    position: absolute;
    left: 150px;
    top: 118px;
    font-family: "Open Sans", sans-serif;
    font-weight: 400;
  }
  .contact__name {
    font-size: 30px;
    letter-spacing: 9px;
    color: var(--brand-orange);
    white-space: nowrap;
  }
  .contact__phone {
    margin-top: 2px;
    font-size: 28px;
    letter-spacing: 7px;
    color: var(--text-light);
    white-space: nowrap;
  }
</style>
</head>
<body>
  <main class="canvas">
    <section class="card card--front" aria-label="Business card front">
      <div class="brand">
        <div class="brand__square"></div>
        <h1 class="brand__name">Brisket Glazing</h1>
      </div>
      <svg class="edge-band" viewBox="0 0 540 38" preserveAspectRatio="none" aria-hidden="true">
        <defs>
          <linearGradient id="silverLine" x1="0" y1="0" x2="1" y2="0">
            <stop offset="0" stop-color="var(--silver-dark)"/>
            <stop offset="0.5" stop-color="var(--silver)"/>
            <stop offset="1" stop-color="var(--silver-dark)"/>
          </linearGradient>
          <linearGradient id="orangeBand" x1="0" y1="0" x2="1" y2="0">
            <stop offset="0" stop-color="var(--orange-deep)"/>
            <stop offset="0.5" stop-color="var(--brand-orange)"/>
            <stop offset="1" stop-color="var(--orange-deep)"/>
          </linearGradient>
        </defs>
        <rect x="0" y="6" width="540" height="6" fill="url(#silverLine)"/>
        <rect x="0" y="12" width="540" height="26" fill="url(#orangeBand)"/>
      </svg>
    </section>

    <section class="card card--back" aria-label="Business card back">
      <div class="accent-square"></div>
      <div class="contact">
        <p class="contact__name">Liam Porter</p>
        <p class="contact__phone">0412 555 730</p>
      </div>
    </section>
  </main>
</body>
</html>
```